Birch Polar Methods Consulting Company Template

Microsoft Word template for a professional retail consulting company that can suggestingly mimic the attached design, but in vertical fashion - . Important - It doesn't have to mimic this design. I accept creativity, professionalism, and eye catching work!

I'd also like suggestingly the globe of the attached logo to appear as an imprint in the background

To win the contest, please make it look extremely impressive, attention grabbing, and don't fear giving it your own creative unique design elements.

The Word template is needed for me to create Word documents from, so it is highly important that I would be able to write memos in Word, and for those same memos to look clean.

Target Market(s)

Retailers interested in consulting services from Birch Toolworks

Font styles to use
Serif

Requirements
Must have
• Birch Polar Methods logo represented. Also, red and black logo colors. A professional, modern, outstanding look and design. Must be somewhat bold and upmarket.
Nice to have
• I accept all forms of creativity.
Should not have
• Cartoon / child looking

```html
<!DOCTYPE html>
<html lang="en">
<head>
<meta charset="utf-8">
<title>Birch Polar Methods Consulting Company – Document Template Set</title>
<link href="https://fonts.googleapis.com/css2?family=Open+Sans:ital,wght@0,300;0,400;0,600;0,700;1,400&display=swap" rel="stylesheet">
<style>
:root{
  --backdrop:#cfcfd1;
  --paper:#ffffff;
  --red:#e31e2d;
  --red-dark:#9e1520;
  --grey:#6a6a6b;
  --grey-dark:#555556;
  --pink:#f8d3d8;
  --pink-soft:#fbe6e9;
  --ink:#333333;
  --muted:#666666;
}
*{margin:0;padding:0;box-sizing:border-box}
html,body{width:1200px;height:1200px;overflow:hidden;background:var(--backdrop)}
body{font-family:"Open Sans",Arial,sans-serif;color:var(--ink)}
.sheet{position:absolute;left:0;top:0;width:1500px;height:1500px;transform:scale(.8);transform-origin:0 0}
.page{position:absolute;width:338px;height:438px;background:var(--paper);overflow:hidden;box-shadow:0 2px 5px rgba(0,0,0,.22)}
.page svg.art{position:absolute;left:0;top:0;width:338px;height:438px}

/* brand lockup */
.brand{position:absolute;display:flex;align-items:center;gap:6px}
.brand .dot{border-radius:50%;background:var(--red);flex:none}
.brand .name{display:block;font-weight:700;color:var(--grey-dark);letter-spacing:.2px;line-height:1;white-space:nowrap}
.brand .tag{display:block;font-weight:600;color:var(--red);letter-spacing:.6px;margin-top:3px;white-space:nowrap}
.brand.lg .dot{width:38px;height:38px}
.brand.lg .name{font-size:17px}
.brand.lg .tag{font-size:6.4px}
.brand.sm .dot{width:11px;height:11px}
.brand.sm{gap:3px}
.brand.sm .name{font-size:6px}
.brand.sm .tag{font-size:2.6px;margin-top:1px;letter-spacing:.2px}

/* cover text */
.cover-title{position:absolute;left:0;width:338px;text-align:center;color:#fff;font-weight:300;font-size:19px;line-height:28px;letter-spacing:.3px}
.cover-sub{position:absolute;left:0;width:338px;text-align:center;color:#f1f1f1;font-size:10.5px;font-weight:400}

.emblem{position:absolute;border-radius:50%}

/* interior header */
.head{position:absolute;left:36px;right:36px;top:20px;height:27px;border-top:1px dotted var(--red);border-bottom:1px dotted var(--red);text-align:center;font-size:11.5px;line-height:25px;color:var(--ink);letter-spacing:.3px;font-weight:400}

/* body copy */
.copy{position:absolute;left:36px;right:36px;font-size:4.6px;line-height:7.3px;color:var(--ink)}
.copy p{margin-bottom:5px}
.copy h3{font-size:8.3px;font-weight:600;line-height:10px;margin:4px 0 1px;color:#222}
.copy h4{font-size:5.6px;font-weight:400;color:var(--red);margin:3px 0 1px}
.copy .lead{color:var(--red-dark);font-style:italic;font-size:5.4px;line-height:7.6px}
.copy .big{font-size:7.8px;line-height:9.6px;color:var(--muted);font-weight:400}
.copy .hot{color:var(--red)}
.copy ul{list-style:none}
.copy li{position:relative;padding-left:6px;margin-bottom:2px}
.copy li::before{content:"";position:absolute;left:0;top:2.3px;width:3px;height:3px;background:var(--red-dark)}
.copy li.sub{padding-left:36px;color:var(--red)}
.copy li.sub::before{left:30px;top:2px;width:0;height:0;background:none;border-left:3.5px solid var(--red);border-top:1.8px solid transparent;border-bottom:1.8px solid transparent}

/* table of contents */
.toc{position:absolute;left:37px;right:37px;top:60px;font-size:4.8px;color:var(--ink)}
.toc h3{font-size:8.5px;font-weight:600;margin-bottom:7px}
.toc .row{display:flex;align-items:flex-end;height:11px}
.toc .row .lbl{white-space:nowrap}
.toc .row .lead-dots{flex:1;border-bottom:1px dotted #999;margin:0 4px 1.5px}
.toc .row .num{width:8px;text-align:right}

/* footer */
.foot{position:absolute;left:0;top:418px;width:338px;height:12px}
.foot .bar{position:absolute;left:0;top:2px;width:192px;height:8px;background:var(--grey);color:#eee;font-size:3.6px;line-height:8px;padding-left:32px}
.foot .brand{left:205px;top:0}
.foot .pg{position:absolute;right:0;top:2px;width:46px;height:8px;background:var(--red-dark);color:#fff;font-size:5.5px;line-height:8px;padding-left:14px}

.photo{position:absolute;background:linear-gradient(135deg,#3b4654 0%,#6f7b88 45%,#c9c4bd 100%)}

/* mission banner */
.mission{position:absolute;left:34px;right:36px;top:60px;height:30px;display:flex}
.mission .icon{width:30px;height:30px;background:var(--red);display:flex;align-items:center;justify-content:center}
.mission .txt{flex:1;background:var(--grey);color:#fff;font-size:5.2px;line-height:6.8px;padding:3px 8px}

/* tables */
.grid{position:absolute;left:36px;width:262px;border-collapse:separate;border-spacing:3px 1.5px;font-size:4.2px;color:var(--ink)}
.grid th{background:var(--red-dark);color:#fff;font-weight:600;height:8px;text-align:center}
.grid td{background:var(--pink-soft);height:8.8px;padding-left:4px}
.grid td.c{text-align:center;padding:0}
.grid tr.phase td{background:var(--pink);color:var(--red);font-weight:600}
.grid tr.total td{background:var(--pink);font-weight:700}
.grid tr.grand td{background:var(--pink);color:var(--red);font-weight:700}

/* contact block */
.contact{position:absolute;display:flex;align-items:center;gap:8px;font-size:4.2px;line-height:7.2px}
.contact .mark{width:22px;height:22px;border-radius:50%;background:var(--red);flex:none}
.contact ul{list-style:none}
.contact li{display:flex;align-items:center;gap:3px;white-space:nowrap}
.contact .ico{width:5px;height:5px;border-radius:50%;background:var(--red);flex:none}
.contact .addr{border-left:1px solid currentColor;padding-left:8px;font-weight:600;white-space:nowrap}
.contact.light{color:#fff}
.contact.light .ico,.contact.light .mark{background:#fff}
.contact.dark{color:var(--ink)}
</style>
</head>
<body>
<div class="sheet">

<!-- Front cover, light -->
<section class="page" style="left:34px;top:40px">
  <svg class="art" viewBox="0 0 338 438" aria-hidden="true">
    <path d="M0 200 Q150 212 338 238 L338 438 L0 438Z" fill="#6a6a6b"/>
    <path d="M0 168 Q170 176 338 208 L338 236 Q170 206 0 198Z" fill="#e31e2d"/>
    <path d="M0 190 Q170 200 338 228 L338 236 Q170 206 0 198Z" fill="#9e1520"/>
  </svg>
  <div class="brand lg" style="left:72px;top:58px">
    <span class="dot"></span>
    <span><span class="name">BIRCH POLAR METHODS</span><span class="tag">INSIGHT | STRATEGY | GROWTH</span></span>
  </div>
  <div class="cover-title" style="top:288px">LOREM IPSUM IS SIMPLY<br>DUMMY HAS BEEN</div>
  <div class="cover-sub" style="top:359px">Lorem Ipsum Is Simply Dummy Has Been</div>
</section>

<!-- Front cover, dark -->
<section class="page" style="left:402px;top:40px;background:var(--grey)">
  <div class="emblem" role="img" aria-label="Faint brand globe emblem" style="left:120px;top:110px;width:220px;height:220px;background:rgba(255,255,255,.05)"></div>
  <svg class="art" viewBox="0 0 338 438" aria-hidden="true">
    <path d="M0 350 L338 252 L338 292 L0 372Z" fill="#e31e2d"/>
    <path d="M0 372 L338 292 L338 438 L0 438Z" fill="#ffffff"/>
    <path d="M0 367 L338 286 L338 292 L0 372Z" fill="#9e1520"/>
  </svg>
  <div class="cover-title" style="top:72px">LOREM IPSUM IS SIMPLY<br>DUMMY HAS BEEN</div>
  <div class="cover-sub" style="top:166px">Lorem Ipsum Is Simply Dummy Has Been</div>
  <div class="brand lg" style="left:78px;top:372px">
    <span class="dot"></span>
    <span><span class="name">BIRCH POLAR METHODS</span><span class="tag">INSIGHT | STRATEGY | GROWTH</span></span>
  </div>
</section>

<!-- Table of contents -->
<section class="page" style="left:772px;top:36px">
  <div class="head">TABLE OF CONTENTS</div>
  <div class="toc">
    <h3>Contents</h3>
    <div class="row"><span class="lbl">Table of Contents</span><span class="lead-dots"></span><span class="num">01</span></div>
    <div class="row"><span class="lbl">Executive Summary</span><span class="lead-dots"></span><span class="num">02</span></div>
    <div class="row"><span class="lbl">Our Understanding of Your Needs</span><span class="lead-dots"></span><span class="num">02</span></div>
    <div class="row"><span class="lbl">Our Recommendations</span><span class="lead-dots"></span><span class="num">03</span></div>
    <div class="row"><span class="lbl">Our Approach</span><span class="lead-dots"></span><span class="num">05</span></div>
    <div class="row"><span class="lbl">Budget and Timeframe</span><span class="lead-dots"></span><span class="num">07</span></div>
    <div class="row"><span class="lbl">Appendix A: About Alder Creek</span><span class="lead-dots"></span><span class="num">10</span></div>
    <div class="row"><span class="lbl">Appendix B: Selected Client List</span><span class="lead-dots"></span><span class="num">10</span></div>
    <div class="row"><span class="lbl">Appendix C: Our Capabilities</span><span class="lead-dots"></span><span class="num">11</span></div>
    <div class="row"><span class="lbl">Appendix D: Our Process</span><span class="lead-dots"></span><span class="num">12</span></div>
  </div>
  <footer class="foot">
    <div class="bar">www.birchpolar.com</div>
    <div class="brand sm"><span class="dot"></span><span><span class="name">BIRCH POLAR METHODS</span><span class="tag">INSIGHT | STRATEGY | GROWTH</span></span></div>
    <div class="pg">01</div>
  </footer>
</section>

<!-- Understanding of needs -->
<section class="page" style="left:1139px;top:36px">
  <div class="head">OUR UNDERSTANDING OF YOUR NEEDS</div>
  <div class="copy" style="top:56px">
    <p>In the last two weeks of January we conducted high level conversations with your staff and your technology partner Northloop. As a result of those conversations we have been able to gather the following high level goals for your project:</p>
    <p class="big">CRMCore must be in place to support Tidewell at launch and as the program evolves</p>
    <p class="lead">The most critical aspect of this implementation both in terms of time sensitivity as well as functionality is centered around the support for the Tidewell project. Our current understanding of this project and how it relates to CRMCore is as follows:</p>
    <ul>
      <li>Tidewell will be comprised of a series of websites focused on organizing institutions and individuals within six specific community sectors with the goal of increased leadership and public support to help communities become better prepared to minimize the risks and maximize opportunities of a changing climate.</li>
      <li>The primary goals of the CRM application are:</li>
      <li class="sub">capture information of individuals and organizations (along with their respective roles)</li>
      <li class="sub">track their progress on their site specific to-do lists and site interactions</li>
      <li class="sub">allow greenPath to push out next steps (ideally in an automated style) related to their to do list progress and online interactions</li>
      <li class="sub">infuse greenPath's online and offline marketing program with useful segmentation information</li>
      <li class="sub">natively integrate with both the Tidewell family of sites as well as greenPath's</li>
      <li>The data architecture must be well defined but flexible to support the core needs of the sites at launch as well as anticipated needs in the future.</li>
      <li class="sub">For instance, the faith based site may collect a "denomination" field, while other sites may not collect that field.</li>
      <li class="sub">Future interactions outside of the to-do list may become necessary to track and greenPath will need a systemic way to capture those interactions, be able to segment on them and potentially provide automated marketing around those similar to the to-do list</li>
      <li>The information collected from the Tidewell sites must be combined with current information held within greenPath and provide a holistic view of institutions and individuals.</li>
    </ul>
  </div>
  <footer class="foot">
    <div class="bar">www.birchpolar.com</div>
    <div class="brand sm"><span class="dot"></span><span><span class="name">BIRCH POLAR METHODS</span><span class="tag">INSIGHT | STRATEGY | GROWTH</span></span></div>
    <div class="pg">04</div>
  </footer>
</section>

<!-- Vision -->
<section class="page" style="left:34px;top:524px">
  <div class="head">VISION</div>
  <div class="mission">
    <div class="icon">
      <svg width="22" height="22" viewBox="0 0 22 22" aria-hidden="true"><circle cx="11" cy="11" r="9" fill="none" stroke="#fff" stroke-width="1.8"/><circle cx="11" cy="11" r="5.5" fill="none" stroke="#fff" stroke-width="1.8"/><circle cx="11" cy="11" r="2" fill="#fff"/></svg>
    </div>
    <div class="txt">Ledgerly's mission is to help and support the self-employed and small business owners with their administrative tasks so they can focus on what matters – their business.</div>
  </div>
  <div class="copy" style="top:102px">
    <p class="lead">Administrative tasks are cumbersome, time-consuming and often prevent small owners from focusing their time and energy on their business and their customers. They can also be extremely stressful and nerve-wracking for those attempting these tasks for the first time.</p>
    <p class="lead hot">At Ledgerly, we envisage accounting for the self-employed and small business owners as being automated and decentralized</p>
    <p>Accounting can and should be done automatically. By connecting to all sources of accounting data such as bank accounts, payment systems, e-commerce websites, and invoicing systems, Ledgerly AI automatically completes these tasks, which would take hours to do manually. Bookings are created automatically and fully completed. Financial statements are available within a couple of clicks, and after analysing your data, Ledgerly AI will offer you tips to improve your financial stability.</p>
    <p>What may seem like a pipedream to the millions of self-employed who struggle with their admin, is already a reality. Now is the time to join Ledgerly on its mission to transform the world of bookkeeping through the power of AI.</p>
    <h3>The Ledgerly model</h3>
    <p>Ledgerly is based on an innovative license model that uses Token-as-a-License (TaaL). The token represents lifelong software license for Ledgerly solutions. The pre-sale token sales will enable Ledgerly to complete its development of Ledgerly AI to deliver fully automatic bookkeeping.</p>
    <p>The token sale will also pave the way for a future Ledgerly offering. Ledgerly will launch accounting on the blockchain and ensure your accounting data is comprehensive and private, but accessible everywhere within your preferred apps. It will empower you to manage your data as you see fit in a fully decentralized way. Furthermore, a new range of business apps will connect to Ledgerly to provide you with leading edge business data access to ensure you have the best available data at your fingertips.</p>
    <p>Ledgerly supports strong data ownership laws that truly protect individuals and ensure they have complete ownership of their data. Through decentralisation Ledgerly helps to ensure you always have full ownership of your data to decide how it should be used.</p>
  </div>
  <footer class="foot">
    <div class="bar">www.birchpolar.com</div>
    <div class="brand sm"><span class="dot"></span><span><span class="name">BIRCH POLAR METHODS</span><span class="tag">INSIGHT | STRATEGY | GROWTH</span></span></div>
    <div class="pg">03</div>
  </footer>
</section>

<!-- Headline with photo -->
<section class="page" style="left:397px;top:524px">
  <div class="head">HEADLINE HERE</div>
  <div class="photo" role="img" aria-label="Photo of a stressed businessman at a desk" style="left:36px;top:59px;width:266px;height:118px"></div>
  <div class="copy" style="top:187px">
    <p class="lead hot" style="font-style:normal">Ledgerly's mission is to help and support the self-employed and small business owners with their administrative tasks so they can focus on what matters – their business.</p>
    <p>Administrative tasks are cumbersome, time-consuming and often prevent small owners from focusing their time and energy on their business and their customers. They can also be extremely stressful and nerve-wracking for those attempting these tasks for the first time.</p>
    <p>At Ledgerly, we envisage accounting for the self-employed and small business owners as being <span class="hot">automated and decentralized</span></p>
    <p>Accounting can and should be done automatically. By connecting to all sources of accounting data such as bank accounts, payment systems, e-commerce websites, and invoicing systems, Ledgerly AI automatically completes these tasks, which would take hours to do manually. Bookings are created automatically and fully completed. Financial statements are available within a couple of clicks, and after analysing your data, Ledgerly AI will offer you tips to improve your financial stability.</p>
    <p>What may seem like a pipedream to the millions of self-employed who struggle with their admin, is already a reality. Now is the time to join Ledgerly on its mission to transform the world of bookkeeping through the power of AI.</p>
    <h3>The Ledgerly model</h3>
    <p>Ledgerly is based on an innovative license model that uses Token-as-a-License (TaaL). The token represents lifelong software license for Ledgerly solutions. The pre-sale token sales will enable Ledgerly to complete its development of Ledgerly AI to deliver fully automatic bookkeeping.</p>
  </div>
  <footer class="foot">
    <div class="bar">www.birchpolar.com</div>
    <div class="brand sm"><span class="dot"></span><span><span class="name">BIRCH POLAR METHODS</span><span class="tag">INSIGHT | STRATEGY | GROWTH</span></span></div>
    <div class="pg">04</div>
  </footer>
</section>

<!-- Headline: solution -->
<section class="page" style="left:768px;top:524px">
  <div class="head">HEADLINE HERE</div>
  <div class="copy" style="top:60px">
    <h3>Solution</h3>
    <h4>AI automated accounting</h4>
    <p>Ledgerly builds automation in stages on top of its current system to reach full automation thanks to the Ledgerly AI. Ledgerly AI automates every manual task performed by the user. It starts by connecting to all sources of accounting data such as bank accounts, payment systems, e-commerce websites, invoicing systems, webshop or document management systems in cloud storage. Based on these datas, Ledgerly AI creates bookings and generates financial reports. Finally, Ledgerly AI features chat-like interface that allows users to communicate seamlessly with it, viewing it as a trusted advisor over time for all their accounting queries.</p>
    <h4>Blockchain software license or Token-as-a-License (TaaL)</h4>
    <p>It is possible to create tokens on blockchain that represent software licenses, also known as Token-as-a-Licence (TaaL). Ledgerly creates TaaL by using the Cinder official wallet which interacts with the Cinder blockchain. Upon purchase of TaaL, the token holder is free to transfer or sell TaaL using secondary market that is built directly over the Cinder marketplace. Ledgerly checks the validity of a token against the blockchain ensuring that token holders have access to the software. TaaL make distribution and securisation of software licenses easier for software developers.</p>
    <h3>Pre-sale Token sale</h3>
    <p>To realize this innovative vision, Ledgerly is launching a pre-sale in form of a token sale on Cinder blockchain. 20,000,000 tokens are available to purchase for the price of 0.10 each during a 30-day period to be announced. Tokens represent Ledgerly lifelong software licenses and by purchasing enough tokens, holders gain access to Ledgerly software. 15,000 tokens give access to Ledgerly invoicing or accounting. 20,000 tokens give access to both Ledgerly accounting and invoicing. Future customers will still have the opportunity to buy directly yearly or monthly subscriptions to have access to Ledgerly.</p>
    <h3>Future plans</h3>
    <p>A future offering is planned between 18 and 24 months after the pre-sale token sale. This offering will support the development of Ledgerly into a fully decentralized, privacy-focused ecosystem of applications. The new model will reward each participant so that a new world with zero</p>
  </div>
  <footer class="foot">
    <div class="bar">www.birchpolar.com</div>
    <div class="brand sm"><span class="dot"></span><span><span class="name">BIRCH POLAR METHODS</span><span class="tag">INSIGHT | STRATEGY | GROWTH</span></span></div>
    <div class="pg">02</div>
  </footer>
</section>

<!-- Budget and timeframe -->
<section class="page" style="left:1139px;top:524px">
  <div class="head">BUDGET AND TIMEFRAME</div>
  <div class="copy" style="top:56px">
    <h3 style="font-size:8.8px">Implementation Estimate</h3>
    <p>The bulk of the implementation costs will be defined by discovery. Based on similar CRM implementation projects, we feel expect that the CRM side will be somewhere between 200 and 300 hours, give or take. The wide swing in hours in phase one is related to the ill-defined nature of both the integration needs and our role in the integration project. Our focus in discovery (as mentioned above) will be to nail down and finalize those requirements and our role as it relates to what is needed to integrate the sites with the CRM.</p>
  </div>
  <table class="grid" style="top:132px">
    <tr><th style="width:132px">Task</th><th>Hours</th><th>Cost</th></tr>
    <tr><td>Discovery</td><td class="c">40</td><td class="c">$8,000</td></tr>
    <tr class="phase"><td colspan="3">Phase 1</td></tr>
    <tr><td>Discovery</td><td class="c">20-40</td><td class="c">$8,000</td></tr>
    <tr><td>Discovery</td><td class="c">20-40</td><td class="c">$8,000</td></tr>
    <tr><td>Discovery</td><td class="c">20-40</td><td class="c">$8,000</td></tr>
    <tr class="total"><td>Total Phase 1</td><td class="c">80-240</td><td class="c">$16,800-40,000</td></tr>
    <tr class="phase"><td colspan="3">Phase 2</td></tr>
    <tr><td>Discovery</td><td class="c">20-40</td><td class="c">$8,000</td></tr>
    <tr class="total"><td>Total Phase 2</td><td class="c">80-240</td><td class="c">$16,800-40,000</td></tr>
    <tr class="grand"><td>Total Estimated Implementation Cost</td><td class="c">220-480</td><td class="c">$44,000-96,000</td></tr>
  </table>
  <div class="copy" style="top:276px">
    <h3 style="font-size:8.8px">Project Timeline</h3>
    <p>Based on the information we have at our disposal, the March 21st launch date doesn't seem a realistic goal to get both the work done needed to provide the foundation for the future CRM instance and the integration given the state of apparent flux of the requirements. That said, we feel it prudent to proceed with discovery before committing to or pushing that date. We are currently estimating that the first phase will take somewhere between 7 and 12 weeks (including discovery) to complete.</p>
  </div>
  <table class="grid" style="top:343px">
    <tr><th style="width:160px">Task</th><th>Weeks to Complete</th></tr>
    <tr><td>Discovery</td><td class="c">1-2</td></tr>
    <tr><td>Phase 1</td><td class="c">6-10</td></tr>
    <tr><td>Phase 2</td><td class="c">8-12</td></tr>
    <tr class="total"><td>Total Number of Weeks</td><td class="c"></td></tr>
  </table>
  <footer class="foot">
    <div class="bar">www.birchpolar.com</div>
    <div class="brand sm"><span class="dot"></span><span><span class="name">BIRCH POLAR METHODS</span><span class="tag">INSIGHT | STRATEGY | GROWTH</span></span></div>
    <div class="pg">04</div>
  </footer>
</section>

<!-- Headline with two photos -->
<section class="page" style="left:34px;top:1007px">
  <div class="head">HEADLINE HERE</div>
  <div class="photo" role="img" aria-label="Photo of a stressed businessman holding his head" style="left:33px;top:61px;width:115px;height:175px"></div>
  <div class="photo" role="img" aria-label="Photo of a businessman looking down at his work" style="left:33px;top:265px;width:115px;height:136px"></div>
  <div class="copy" style="top:60px;left:164px;right:36px">
    <p class="lead hot">Ledgerly's mission is to help and support the self-employed and small business owners with their administrative tasks so they can focus on what matters – their business.</p>
    <p>Administrative tasks are cumbersome, time-consuming and often prevent small owners from focusing their time and energy on their business and their customers. They can also be extremely stressful and nerve-wracking for those attempting these tasks for the first time.</p>
    <p>At Ledgerly, we envisage accounting for the self-employed and small business owners as being <span class="hot" style="font-style:italic">automated and decentralized</span></p>
    <p>Accounting can and should be done automatically. By connecting to all sources of accounting data such as bank accounts, payment systems, e-commerce websites, and invoicing systems, Ledgerly AI automatically completes these tasks, which would take hours to do manually. Bookings are created automatically and fully completed. Financial statements are available within a couple of clicks, and after analysing your data, Ledgerly AI will offer you tips to improve your financial stability.</p>
    <p>What may seem like a pipedream to the millions of self-employed who struggle with</p>
    <h3>The Ledgerly model</h3>
    <p>Ledgerly is based on an innovative license model that uses Token-as-a-License (TaaL). The token represents lifelong software license for Ledgerly solutions. The pre-sale token sales will enable Ledgerly to complete its development of Ledgerly AI to deliver fully automatic bookkeeping.</p>
  </div>
  <footer class="foot">
    <div class="bar">www.birchpolar.com</div>
    <div class="brand sm"><span class="dot"></span><span><span class="name">BIRCH POLAR METHODS</span><span class="tag">INSIGHT | STRATEGY | GROWTH</span></span></div>
    <div class="pg">04</div>
  </footer>
</section>

<!-- Back cover, light -->
<section class="page" style="left:397px;top:1007px">
  <div class="emblem" role="img" aria-label="Large soft pink brand globe emblem" style="left:30px;top:16px;width:255px;height:255px;background:radial-gradient(circle at 40% 35%,#fbe2e6 0%,#f5c2ca 70%,#f0b3bd 100%)"></div>
  <svg class="art" viewBox="0 0 338 438" aria-hidden="true">
    <path d="M0 275 Q170 270 338 288 L338 438 L0 438Z" fill="#6a6a6b"/>
    <path d="M0 262 Q170 255 338 268 L338 292 Q170 276 0 283Z" fill="#e31e2d"/>
    <path d="M0 276 Q170 268 338 282 L338 292 Q170 276 0 283Z" fill="#9e1520"/>
  </svg>
  <div class="contact light" style="left:64px;top:374px">
    <span class="mark"></span>
    <ul>
      <li><span class="ico"></span>000-555-0142 Ext 101</li>
      <li><span class="ico"></span>hello@birchpolar.com</li>
      <li><span class="ico"></span>www.birchpolar.com</li>
    </ul>
    <div class="addr">210, 48 Larch Avenue<br>Fernvale Province QQQ 4821</div>
  </div>
</section>

<!-- Back cover, dark -->
<section class="page" style="left:772px;top:1007px;background:var(--grey)">
  <div class="emblem" role="img" aria-label="Faint brand globe emblem" style="left:110px;top:95px;width:220px;height:220px;background:rgba(255,255,255,.05)"></div>
  <svg class="art" viewBox="0 0 338 438" aria-hidden="true">
    <path d="M0 345 L338 252 L338 292 L0 370Z" fill="#e31e2d"/>
    <path d="M0 370 L338 292 L338 438 L0 438Z" fill="#ffffff"/>
    <path d="M0 364 L338 286 L338 292 L0 370Z" fill="#9e1520"/>
  </svg>
  <div class="contact dark" style="left:70px;top:386px">
    <span class="mark"></span>
    <ul>
      <li><span class="ico"></span>000-555-0142 Ext 101</li>
      <li><span class="ico"></span>hello@birchpolar.com</li>
      <li><span class="ico"></span>www.birchpolar.com</li>
    </ul>
    <div class="addr">210, 48 Larch Avenue<br>Fernvale Province QQQ 4821</div>
  </div>
</section>

</div>
</body>
</html>
```